tolv Marketing Brochure for construction of multi-million dollar homes in the Caribbean

Design a marketing brochure for a construction company operating in the Caribbean for ultra high-end signature homes and villas. Target audience is ultra high net worth individuals, families, international property developers and hotel chains. We have provided an our marketing brochure for reference but would like a totally new look and feel with updated wording and photos (also provided). The company logo of light and dark blue circles and 'tolv' with the 's' in superscript must feature throughout. Further information can be extracted from the company's website: tolvharbour.example. Depending on how this goes there may be additional projects such as website and log redesign. Thanks!

Target Market(s)

Target audience is ultra high net worth individuals, families, international property developers and hotel chains.

Font styles to use
Other font styles liked:
• see logo for desired phones

Colors
3aa7d7
0655a3
85cae6
3176b5
85acd3
33a6d7
cee9f5
cedeed

Requirements
Must have
• Detailed company info including projects and employee profiles - must be bold, brilliant and eye-catching.
Nice to have
• Colour
Should not have
• Too much info.

```html
<!DOCTYPE html>
<html lang="en">
<head>
<meta charset="utf-8">
<title>tolv brochure spreads</title>
<link href="https://fonts.googleapis.com/css2?family=Marcellus&family=Raleway:wght@400;500&display=swap" rel="stylesheet">
<style>
  :root {
    --backdrop: #76687c;
    --navy: #2e3192;
    --teal: #7ecfd0;
    --rule: #7b80c0;
    --ink-grey: #5a5a5a;
    --dark-bar: #2a2a2e;
    --paper: #ffffff;
  }
  * { box-sizing: border-box; margin: 0; padding: 0; }
  html, body { width: 1200px; height: 956px; overflow: hidden; }
  body { background: var(--backdrop); position: relative; font-family: "Raleway", sans-serif; }

  .page { position: absolute; width: 545px; height: 385px; background: var(--paper); overflow: hidden; box-shadow: 0 3px 10px rgba(0,0,0,.35); }
  .page--cover { left: 49px; top: 73px; }
  .page--welcome { left: 616px; top: 73px; }
  .page--design { left: 49px; top: 483px; }
  .page--cost { left: 616px; top: 483px; }

  .photo { position: absolute; }
  .cover-art { position: absolute; inset: 0; }
  .cover-tagline { position: absolute; left: 33px; top: 24px; color: #fff; font-family: "Marcellus", serif; font-size: 16px; line-height: 1.2; letter-spacing: .3px; }
  .cover-brand { position: absolute; left: 262px; top: 292px; display: flex; align-items: center; gap: 18px; }
  .cover-brand .mark { width: 58px; height: 58px; border-radius: 50%; background: var(--navy); }
  .cover-brand .name { font-family: "Marcellus", serif; font-size: 64px; color: var(--ink-grey); line-height: 1; }

  .header { position: absolute; left: 22px; right: 18px; top: 12px; height: 30px; }
  .header .brand { position: absolute; left: 0; top: 0; display: flex; align-items: center; gap: 6px; }
  .header .brand .mark { width: 14px; height: 14px; border-radius: 50%; background: var(--navy); }
  .header .brand .name { font-family: "Marcellus", serif; font-size: 23px; color: var(--ink-grey); line-height: 1; }
  .header .rule { position: absolute; left: 78px; right: 0; top: 23px; height: 1px; background: var(--rule); }
  .header .tagline { position: absolute; right: 0; top: 7px; font-family: "Marcellus", serif; font-size: 9px; line-height: 1.2; color: var(--navy); }

  .side-bar { position: absolute; left: 17px; width: 5px; }
  .side-bar .teal { background: var(--teal); width: 100%; height: 26px; }
  .side-bar .navy { background: var(--navy); width: 100%; }

  .footer { position: absolute; left: 0; bottom: 0; width: 545px; height: 12px; }

  .welcome-box { position: absolute; left: 369px; top: 50px; width: 159px; height: 250px; background: var(--navy); color: #fff; padding: 12px 10px 0 10px; }
  .welcome-box h2 { font-family: "Marcellus", serif; font-weight: 400; font-size: 18px; line-height: 1.2; text-align: center; margin-bottom: 10px; letter-spacing: .5px; }
  .welcome-box p { font-size: 7.3px; line-height: 12.3px; margin-bottom: 12px; }

  .section-title { position: absolute; font-family: "Marcellus", serif; font-weight: 400; font-size: 19px; line-height: 1; color: var(--navy); white-space: nowrap; }
  .section-body { position: absolute; color: var(--navy); font-size: 7.4px; font-weight: 400; line-height: 12.3px; }
</style>
</head>
<body>

<section class="page page--cover">
  <svg class="cover-art" width="545" height="385" viewBox="0 0 545 385">
    <polygon points="0,0 545,0 545,34 0,98" fill="var(--navy)"/>
    <polygon points="170,78 545,32 545,48 0,110 0,98" fill="var(--teal)"/>
    <polygon points="0,98 545,48 545,252 0,312" fill="var(--navy)"/>
    <polygon points="0,312 545,246 545,258 70,310" fill="var(--teal)"/>
    <polygon points="0,312 545,252 545,262 0,322" fill="var(--navy)"/>
  </svg>
  <svg class="photo" style="left:0;top:0" width="545" height="385" viewBox="0 0 545 385" role="img" aria-label="Photo: open villa terrace with lounge furniture overlooking the sea">
    <defs>
      <linearGradient id="coverPhoto" x1="0" y1="0" x2="0" y2="1">
        <stop offset="0" stop-color="#8fb9de"/>
        <stop offset=".35" stop-color="#c9dced"/>
        <stop offset=".5" stop-color="#3e75ad"/>
        <stop offset=".7" stop-color="#d9d2c4"/>
        <stop offset="1" stop-color="#b9ab96"/>
      </linearGradient>
    </defs>
    <polygon points="0,110 545,48 545,248 0,306" fill="url(#coverPhoto)"/>
  </svg>
  <div class="cover-tagline">design . build . deliver</div>
  <div class="cover-brand"><span class="mark"></span><span class="name">tolv</span></div>
</section>

<section class="page page--welcome">
  <header class="header">
    <div class="brand"><span class="mark"></span><span class="name">tolv</span></div>
    <div class="tagline">design . build . deliver</div>
    <div class="rule"></div>
  </header>
  <div class="side-bar" style="top:50px"><div class="teal"></div><div class="navy" style="height:263px"></div></div>
  <svg class="photo" style="left:24px;top:50px" width="504" height="289" role="img" aria-label="Photo: covered poolside pavilion with dining table, palms and sea view">
    <defs>
      <linearGradient id="welcomePhoto" x1="0" y1="0" x2="0" y2="1">
        <stop offset="0" stop-color="#6b3d22"/>
        <stop offset=".25" stop-color="#5e8fc2"/>
        <stop offset=".5" stop-color="#4f7a3a"/>
        <stop offset=".7" stop-color="#b79a78"/>
        <stop offset="1" stop-color="#c9b9a3"/>
      </linearGradient>
    </defs>
    <rect width="504" height="289" fill="url(#welcomePhoto)"/>
  </svg>
  <div class="welcome-box">
    <h2>WELCOME</h2>
    <p>If you are looking to build your ultimate dream home in your own piece of paradise, tolv Harbour Ltd ("tolv") can not only make it a reality, but can do it in a way that is seamless and specifically tailored for you and your needs. tolv covers all aspects of the building process, from conceptual project planning and design, through to completion and everything in between.</p>
    <p>Specialising in creating luxurious private residences throughout the Caribbean, tolv has built an enviable portfolio of breathtaking villas and opulent homes for extremely satisfied clientele.</p>
  </div>
  <svg class="footer" viewBox="0 0 545 12"><rect x="0" y="7" width="545" height="5" fill="var(--dark-bar)"/><polygon points="0,0 135,0 142,12 0,12" fill="var(--navy)"/><polygon points="139,0 167,0 174,12 146,12" fill="var(--teal)"/></svg>
</section>

<section class="page page--design">
  <header class="header">
    <div class="brand"><span class="mark"></span><span class="name">tolv</span></div>
    <div class="tagline">design . build . deliver</div>
    <div class="rule"></div>
  </header>
  <div class="side-bar" style="top:52px"><div class="teal"></div><div class="navy" style="height:282px"></div></div>
  <svg class="photo" style="left:24px;top:52px" width="283" height="178" role="img" aria-label="Photo: hillside villas on a rocky headland above deep blue sea">
    <defs><linearGradient id="designPhotoA" x1="0" y1="0" x2="0" y2="1"><stop offset="0" stop-color="#3f7fc6"/><stop offset=".3" stop-color="#9aa7b8"/><stop offset=".55" stop-color="#8a6a4a"/><stop offset=".65" stop-color="#1f5a96"/><stop offset="1" stop-color="#174677"/></linearGradient></defs>
    <rect width="283" height="178" fill="url(#designPhotoA)"/>
  </svg>
  <svg class="photo" style="left:312px;top:52px" width="226" height="178" role="img" aria-label="Photo: freestanding bathtub before floor-to-ceiling windows with sea view">
    <defs><linearGradient id="designPhotoB" x1="0" y1="0" x2="1" y2="1"><stop offset="0" stop-color="#8a8466"/><stop offset=".4" stop-color="#6aa3d6"/><stop offset=".7" stop-color="#d8d6cf"/><stop offset="1" stop-color="#3a3630"/></linearGradient></defs>
    <rect width="226" height="178" fill="url(#designPhotoB)"/>
  </svg>
  <h2 class="section-title" style="left:99px;top:280px;">DESIGN REVIEW</h2>
  <p class="section-body" style="left:99px;top:305px;width:385px;">Upon completion of the construction documents, tolv strategically review all drawings and specifications with any inefficiencies or irregularities reported to the client before this documentation is submitted to local planning authorities for building approval.</p>
  <svg class="footer" viewBox="0 0 545 12"><rect x="0" y="7" width="545" height="5" fill="var(--dark-bar)"/><polygon points="0,0 135,0 142,12 0,12" fill="var(--navy)"/><polygon points="139,0 167,0 174,12 146,12" fill="var(--teal)"/></svg>
</section>

<section class="page page--cost">
  <header class="header">
    <div class="brand"><span class="mark"></span><span class="name">tolv</span></div>
    <div class="tagline">design . build . deliver</div>
    <div class="rule"></div>
  </header>
  <div class="side-bar" style="top:52px"><div class="teal"></div><div class="navy" style="height:282px"></div></div>
  <h2 class="section-title" style="left:35px;top:87px;">Cost Planning, Budgeting &amp; Value Engineering</h2>
  <p class="section-body" style="left:35px;top:113px;width:482px;">tolv can undertake vital cost analysis on the client's behalf and budgets are meticulously prepared based on the agreed scope of works. Upon evaluation of the budget, tolv undertakes a 'value engineering' exercise where alternate material selections, construction methodologies and project scheduling are adjusted to manage the ultimate cost of the project, without compromising on quality and service delivery.</p>
  <svg class="photo" style="left:29px;top:200px" width="264" height="151" role="img" aria-label="Photo: bright living room with chandelier and open sea views">
    <defs><linearGradient id="costPhotoA" x1="0" y1="0" x2="0" y2="1"><stop offset="0" stop-color="#e6e1d6"/><stop offset=".35" stop-color="#7ea9d6"/><stop offset=".55" stop-color="#3c6ea8"/><stop offset=".75" stop-color="#ebe7df"/><stop offset="1" stop-color="#cfc8bb"/></linearGradient></defs>
    <rect width="264" height="151" fill="url(#costPhotoA)"/>
  </svg>
  <svg class="photo" style="left:298px;top:200px" width="224" height="151" role="img" aria-label="Photo: green-roofed villa set into a cliff above turquoise water">
    <defs><linearGradient id="costPhotoB" x1="0" y1="0" x2="1" y2="1"><stop offset="0" stop-color="#bcd2e6"/><stop offset=".3" stop-color="#2f72b8"/><stop offset=".6" stop-color="#6b7a3e"/><stop offset="1" stop-color="#3f6a2b"/></linearGradient></defs>
    <rect width="224" height="151" fill="url(#costPhotoB)"/>
  </svg>
  <svg class="footer" viewBox="0 0 545 12"><rect x="0" y="7" width="545" height="5" fill="var(--dark-bar)"/><polygon points="0,0 135,0 142,12 0,12" fill="var(--navy)"/><polygon points="139,0 167,0 174,12 146,12" fill="var(--teal)"/></svg>
</section>

</body>
</html>
```